Building Servicess

We need a new business card design for a company. We specialise in: Electrical/Site temporary electrics, Data/Network Installation, Passive Fire Protection

Industry/Entity Type

Construction

Contact Information for Business Card

Services provided as detailed on project description

Font styles to use
Serif

Colors
0054AA
0677BA
7BADD7
CADEEF
E8F1F8
00AB8E
00BBA5
67D7C9
C6EFE9
E9F9F6
EB3D1F
EC4F4E
F09395
F8D3D4
FCEDEE

Requirements
Must have
• Company logo-contact details-phone numbers

```html
<!DOCTYPE html>
<html lang="en">
<head>
<meta charset="utf-8">
<title>Norvale Site Services – Business Card</title>
<link rel="stylesheet" href="https://fonts.googleapis.com/css2?family=Montserrat:wght@600&family=Source+Sans+3:wght@300;400;700&display=swap">
<style>
  :root {
    --blue-top: #368ccb;
    --blue-bottom: #1674bb;
    --blue-deep: #0677ba;
    --white: #ffffff;
    --card-white: #fdfdfe;
    --ink-grey: #4a4f55;
    --canvas: #dfe3e6;
    --divider: rgba(255,255,255,0.55);
  }
  * { margin: 0; padding: 0; box-sizing: border-box; }
  html, body {
    width: 928px; height: 1200px; overflow: hidden;
    background: var(--canvas);
  }
  .canvas { position: relative; width: 928px; height: 1200px; }

  .card {
    position: absolute; left: 124px; width: 679px; height: 389px;
    border-radius: 17px; overflow: hidden;
  }

  /* Shared wordmark */
  .brand {
    position: absolute; display: flex; align-items: center; gap: 8px;
    font-family: "Montserrat", sans-serif; font-weight: 600; letter-spacing: 0.02em;
    font-size: 15px; line-height: 18px; white-space: nowrap;
  }
  .brand__square {
    width: 14px; height: 14px; background: currentColor; flex: none;
  }

  /* Front face */
  .card--front {
    top: 165px;
    background: linear-gradient(180deg, var(--blue-top) 0%, var(--blue-top) 35%, var(--blue-bottom) 100%);
  }
  .card--front .brand {
    left: 212px; top: 195px; transform: translate(-50%, -50%);
    color: var(--white);
  }
  .card__divider {
    position: absolute; left: 369px; top: 97px; width: 1px; height: 198px;
    background: linear-gradient(180deg, transparent, var(--divider) 20%, var(--divider) 80%, transparent);
  }
  .services {
    position: absolute; left: 408px; top: 127px;
    font-family: "Source Sans 3", sans-serif; color: var(--white);
    font-size: 31px; line-height: 34px; list-style: none;
  }
  .services__item { font-weight: 700; }
  .services__item--light { font-weight: 300; }

  /* Back face */
  .card--back {
    top: 638px; background: var(--card-white);
  }
  .name-band {
    position: absolute; left: 0; top: 24px; width: 100%; height: 57px;
    background: linear-gradient(90deg, var(--blue-top), var(--blue-bottom));
    padding: 8px 0 0 24px; color: var(--white);
  }
  .name-band__name {
    font-family: "Montserrat", sans-serif; font-weight: 600;
    font-size: 19px; line-height: 22px;
  }
  .name-band__title {
    font-family: "Source Sans 3", sans-serif; font-weight: 400;
    font-size: 16px; line-height: 18px;
  }
  .card--back .brand {
    right: 24px; top: 128px; color: var(--blue-deep);
  }
  .contacts {
    position: absolute; left: 24px; top: 284px; list-style: none;
    font-family: "Source Sans 3", sans-serif; font-size: 14px; color: var(--ink-grey);
  }
  .contacts__row { height: 22px; line-height: 22px; }
  .contacts__label { display: inline-block; width: 22px; color: var(--blue-deep); }
</style>
</head>
<body>
<main class="canvas">

  <section class="card card--front" aria-label="Card front">
    <div class="brand"><span class="brand__square"></span>NORVALE SITE SERVICES</div>
    <div class="card__divider"></div>
    <ul class="services">
      <li class="services__item">Fire-Stoping</li>
      <li class="services__item">Networking</li>
      <li class="services__item">Electrical</li>
      <li class="services__item services__item--light">Services</li>
    </ul>
  </section>

  <section class="card card--back" aria-label="Card back">
    <div class="name-band">
      <p class="name-band__name">DANIEL MERCER HALE</p>
      <p class="name-band__title">Business Owner</p>
    </div>
    <div class="brand"><span class="brand__square"></span>NORVALE SITE SERVICES</div>
    <ul class="contacts">
      <li class="contacts__row"><span class="contacts__label">c :</span>+44 7700 900123</li>
      <li class="contacts__row"><span class="contacts__label">e :</span>info@norvalesite.co.uk</li>
      <li class="contacts__row"><span class="contacts__label">s :</span>www.norvalesite.co.uk</li>
      <li class="contacts__row"><span class="contacts__label">a :</span>Marlow Crescent, Ashbury, Kent, TN12 4QX</li>
    </ul>
  </section>

</main>
</body>
</html>
```